7 page website for Dog Training Business

we are seeking a website design that should be 7 pages for a Las Vegas Dog training business. the site will have a heavy focus on video, and social media. Ideas design can be borrowed from http://plumcrestway.net
attached is a copy of the logo and business card mock up. Content is currently being written and will be posted shortly

Training

```html
<!DOCTYPE html>
<html lang="en">
<head>
<meta charset="utf-8">
<title>Harlow Dog Training</title>
<link href="https://fonts.googleapis.com/css2?family=Oswald:wght@300;400&family=Open+Sans:wght@400;600&display=swap" rel="stylesheet">
<style>
:root{
  --page-bg:#eee2c9;
  --green:#b5cf4e;
  --green-dark:#7a9b2a;
  --brown:#6d3f1f;
  --charcoal:#333;
  --forest:#3d5a36;
  --header-bg:#3a2a1c;
  --text:#555;
  --muted:#888;
  --band:#f1efe7;
  --footer-light:#f3f3f3;
  --black:#000;
  --white:#fff;
}
*{box-sizing:border-box;margin:0;padding:0}
html,body{width:1200px;height:2195px;overflow:hidden}
body{background:var(--page-bg);font-family:'Open Sans',sans-serif;color:var(--text);position:relative}
.page{position:absolute;left:100px;top:29px;width:1000px;height:2139px;background:var(--white);box-shadow:0 0 12px rgba(0,0,0,.15)}
.header{position:absolute;left:0;top:0;width:1000px;height:154px;background:linear-gradient(180deg,#2e2016,#4a3422)}
.social-top{position:absolute;left:27px;top:55px;display:flex;gap:10px}
.ring{width:37px;height:37px;border:2px solid var(--white);border-radius:50%;display:flex;align-items:center;justify-content:center}
.contact-top{position:absolute;right:82px;top:55px;text-align:right;color:var(--white);font-size:13px;line-height:21px}
.phone-ring{position:absolute;right:27px;top:55px}
.nav{position:absolute;left:0;top:154px;width:1000px;height:56px;background:var(--green);display:flex;align-items:center;font-family:'Oswald',sans-serif;font-weight:300;font-size:15px;color:var(--white);text-transform:uppercase}
.nav a{color:var(--white);text-decoration:none;position:absolute;top:19px}
.logo{position:absolute;left:427px;top:81px;width:146px;height:146px;border-radius:50%;background:var(--green);border:5px solid var(--white);box-shadow:0 0 0 3px var(--green-dark);display:flex;align-items:center;justify-content:center;font-family:'Oswald',sans-serif;font-weight:400;font-size:40px;color:var(--white);z-index:2}
.hero{position:absolute;left:26px;top:237px;width:948px;height:473px;background:linear-gradient(180deg,#a9b9cc 0%,#c4cbd0 45%,#6f8f3c 70%,#4e6e25 100%)}
.hero-title{position:absolute;left:557px;top:265px;font-family:'Oswald',sans-serif;font-size:44px;color:var(--white);text-transform:uppercase;font-weight:400}
.hero-title span{color:var(--green)}
.hero-sub{position:absolute;left:559px;top:322px;width:380px;color:var(--white);font-size:14.5px;line-height:22px;font-weight:600}
.hero-arrows{position:absolute;left:557px;top:383px;display:flex;gap:8px}
.hero-arrows div{width:34px;height:34px;border-radius:50%;background:rgba(0,0,0,.35);display:flex;align-items:center;justify-content:center}
.welcome{position:absolute;left:0;top:735px;width:1000px;height:161px;background:var(--band);text-align:center}
.welcome h1{font-family:'Oswald',sans-serif;font-weight:400;font-size:33px;color:#4a4a3a;margin-top:18px}
.welcome h1 span{color:var(--green-dark)}
.welcome p{width:790px;margin:14px auto 0;font-size:11.5px;line-height:21px;color:#666}
.dvd{position:absolute;left:26px;top:928px;width:330px}
.dvd h2{font-family:'Oswald',sans-serif;font-weight:400;font-size:17px;color:var(--forest);text-transform:uppercase}
.dvd h3{font-weight:400;font-size:15px;line-height:25px;color:#333;margin-top:10px}
.dvd p{font-size:11.5px;line-height:22px;color:#666;margin-top:14px}
.btn{display:inline-block;margin-top:22px;border:1px solid #555;border-radius:4px;padding:9px 12px;font-size:12px;color:#333;text-transform:uppercase}
.video{position:absolute;top:933px;width:280px}
.video .thumb{height:187px;border:4px solid var(--white);box-shadow:0 0 0 1px #ddd;position:relative;display:flex;align-items:center;justify-content:center}
.video .title{margin-top:20px;font-size:15px;color:#444}
.video .date{margin-top:10px;font-size:12px;color:#666;display:flex;align-items:center;gap:8px}
.divider{position:absolute;left:26px;top:1229px;width:948px;height:2px;background:#eee}
.divider::after{content:"";position:absolute;left:466px;top:-3px;width:16px;height:8px;background:var(--white);border:1px solid #ddd}
.cards{position:absolute;left:26px;top:1273px;width:948px;display:flex;gap:22px}
.card{width:220px;background:#f7f7f7}
.card .head{height:50px;display:flex;align-items:center;justify-content:center;font-family:'Oswald',sans-serif;font-weight:300;font-size:17px;color:var(--white)}
.card .img{height:152px}
.card p{padding:16px 14px 18px;font-size:11px;line-height:20px;text-align:center;color:#666}
.quote{position:absolute;left:60px;top:1610px;width:880px;font-size:11.5px;line-height:20px;text-align:center;color:#666}
.qmark{position:absolute;font-family:Georgia,serif;font-size:30px;color:#777}
.testi-band{position:absolute;left:0;top:1778px;width:1000px;height:83px;background:var(--band)}
.avatar{position:absolute;left:418px;top:1712px;width:134px;height:134px;border-radius:50%;border:5px solid var(--white);box-shadow:0 2px 8px rgba(0,0,0,.25);background:linear-gradient(160deg,#6e9a4e,#d9c3a8)}
.author{position:absolute;left:842px;top:1745px;font-size:15px;color:var(--green)}
.info{position:absolute;left:0;top:1861px;width:1000px;height:139px;background:var(--footer-light)}
.badges{position:absolute;left:154px;top:30px;display:flex;gap:4px}
.badges div{width:48px;height:48px;border-radius:50%;background:#d9d0c0;border:2px solid #c9a33a}
.member{position:absolute;left:150px;top:88px;font-family:'Oswald',sans-serif;font-size:11px;color:var(--brown)}
.info-icon{position:absolute;width:56px;height:56px;border-radius:50%;background:var(--white);display:flex;align-items:center;justify-content:center}
.info-text{position:absolute;font-size:13px;line-height:26px;color:#555}
.footer{position:absolute;left:0;top:2000px;width:1000px;height:139px;background:var(--black);text-align:center;color:var(--white)}
.footer nav{margin-top:24px;font-size:12px;text-transform:uppercase}
.footer .copy{margin-top:16px;font-size:11.5px}
.footer .social{display:flex;justify-content:center;gap:6px;margin-top:16px}
.footer .social div{width:29px;height:29px;border:1.5px solid var(--white);border-radius:50%}
</style>
</head>
<body>
<div class="page">
  <header class="header" role="img" aria-label="Dusky photo of a trainer silhouetted with a dog"></header>
  <div class="social-top">
    <div class="ring"></div><div class="ring"></div>
    <div class="ring"><svg width="14" height="18" viewBox="0 0 14 18"><path d="M7 1a6 6 0 0 0-6 6c0 4.5 6 10 6 10s6-5.5 6-10a6 6 0 0 0-6-6z" fill="none" stroke="#fff" stroke-width="2"/><circle cx="7" cy="7" r="2" fill="#fff"/></svg></div>
  </div>
  <div class="contact-top">Phone : +702 - 555 - 0147<br>E-mail : hello@harlowk9.com</div>
  <div class="ring phone-ring"><svg width="16" height="16" viewBox="0 0 24 24"><path d="M6.6 10.8a15 15 0 0 0 6.6 6.6l2.2-2.2a1 1 0 0 1 1-.25 11 11 0 0 0 3.6.6 1 1 0 0 1 1 1V20a1 1 0 0 1-1 1A17 17 0 0 1 3 4a1 1 0 0 1 1-1h3.5a1 1 0 0 1 1 1 11 11 0 0 0 .6 3.6 1 1 0 0 1-.25 1z" fill="#fff"/></svg></div>
  <nav class="nav">
    <a style="left:26px">Home</a><a style="left:127px">About</a><a style="left:198px">Services</a><a style="left:301px">Photos / Videos</a>
    <a style="left:607px">FAQ</a><a style="left:678px">Testimonials</a><a style="left:800px">Store</a><a style="left:897px">Contact Us</a>
  </nav>
  <div class="logo">HARLOW</div>

  <section class="hero" role="img" aria-label="Photo of a white and brown dog running across grass toward a trainer">
    <h2 class="hero-title">Harlow <span>Dog</span> Training</h2>
    <p class="hero-sub">Sed ut perspiciatis unde omnis iste natus error sit voluptatem accusantium doloremque</p>
    <div class="hero-arrows">
      <div><svg width="10" height="14"><path d="M8 1 2 7l6 6" stroke="#fff" stroke-width="2" fill="none"/></svg></div>
      <div><svg width="10" height="14"><path d="m2 1 6 6-6 6" stroke="#fff" stroke-width="2" fill="none"/></svg></div>
    </div>
  </section>

  <section class="welcome">
    <h1>Welcome To <span>Harlow</span></h1>
    <p>Vestibulum commodo volutpat a, convallis ac, laoreet enim. Phasellus fermentum in, dolor pellentesque. Mulla imperdiet sit amet magna. Vestibulum dapibus, Vestibulum commodo volutpat a, convallis ac, laoreet enim. Phasellus fermentum in, dolor pellentesque. Mulla imperdiet sit amet magna. Vestibulum dapibus, Vestibulum commodo volutpat a, convallis ac, laoreet enim. Phasellus fermentum in,</p>
  </section>

  <section class="dvd">
    <h2>Harlow Training DVD Series</h2>
    <h3>Learn to Train Harlow Way: The Foundation + Training Workbook PDF</h3>
    <p>Lorem ipsum dolor sit amet, consectetur adipisicing elit, sed do eiusmod tempor incididunt ut labore et dolore magna aliqua. Ut enim ad minim veniam, quis nostrud exercitation ullamco laboris nisi ut aliquip ex ea commodo</p>
    <span class="btn">Read More Video</span>
  </section>

  <div class="video" style="left:361px">
    <div class="thumb" role="img" aria-label="Video still of a golden retriever on a lawn" style="background:linear-gradient(135deg,#7fb02e,#c9a25a)">
      <svg width="80" height="80"><circle cx="40" cy="40" r="36" fill="rgba(255,255,255,.7)"/><path d="M32 26v28l22-14z" fill="#e0a33a"/></svg>
    </div>
    <div class="title">Set ipsum dolor sit amet</div>
    <div class="date"><svg width="11" height="11"><rect x="0.5" y="2" width="10" height="8.5" fill="#444"/></svg>11 months ago</div>
  </div>
  <div class="video" style="left:669px">
    <div class="thumb" role="img" aria-label="Video still of a trainer and dog silhouetted at sunset" style="background:linear-gradient(180deg,#f0a040,#c8501a 70%,#3a1a0a)">
      <svg width="80" height="80"><circle cx="40" cy="40" r="36" fill="rgba(255,255,255,.7)"/><path d="M32 26v28l22-14z" fill="#e0a33a"/></svg>
    </div>
    <div class="title">Set ipsum dolor sit amet</div>
    <div class="date"><svg width="11" height="11"><rect x="0.5" y="2" width="10" height="8.5" fill="#444"/></svg>11 months ago</div>
  </div>

  <div class="divider"></div>

  <section class="cards">
    <article class="card"><div class="head" style="background:var(--brown)">Dog to Dog Aggression</div><div class="img" role="img" aria-label="Photo of a man kneeling with a dog among autumn leaves" style="background:linear-gradient(160deg,#5a86b8,#c8752a)"></div><p>Lorem ipsum dolor sit amet, conse adipiscing elit. Sed blandit massa vel mauris massa vel</p></article>
    <article class="card"><div class="head" style="background:var(--charcoal)">Dog to Dog Aggression</div><div class="img" role="img" aria-label="Photo of a dog on a leash beside its owner" style="background:linear-gradient(160deg,#d8dce0,#4a5a7a)"></div><p>Lorem ipsum dolor sit amet, conse adipiscing elit. Sed blandit massa vel mauris massa vel</p></article>
    <article class="card"><div class="head" style="background:var(--green)">Dog to Dog Aggression</div><div class="img" role="img" aria-label="Photo of a woman walking a small dog in a park" style="background:linear-gradient(160deg,#7aa84a,#c9c6b4)"></div><p>Lorem ipsum dolor sit amet, conse adipiscing elit. Sed blandit massa vel mauris massa vel</p></article>
    <article class="card"><div class="head" style="background:var(--forest)">Dog to Dog Aggression</div><div class="img" role="img" aria-label="Photo of a child playing with a husky puppy on grass" style="background:linear-gradient(160deg,#a6c25a,#6e8f2a)"></div><p>Lorem ipsum dolor sit amet, conse adipiscing elit. Sed blandit massa vel mauris massa vel</p></article>
  </section>

  <span class="qmark" style="left:55px;top:1600px">&ldquo;</span>
  <p class="quote">Lorem ipsum dolor sit amet, consectetur adipiscing elit, sed do eiusmod tempor incididunt ut labore et dolore magna aliqua. Ut enim ad minim veniam, quis nostrud exercitation ullamco laboris nisi ut aliquip ex ea commodo consequat. Duis aute irure dolor in reprehenderit in voluptate velit esse cillum dolore eu fugiat nulla paatur. Excepteur sint occaecat cupidatat non proident, sunt in culpa qui officia deserunt mollit anim id est laborum</p>
  <span class="qmark" style="left:900px;top:1655px">&rdquo;</span>

  <div class="testi-band"></div>
  <svg style="position:absolute;left:374px;top:1768px" width="12" height="24"><path d="M10 2 2 12l8 10" stroke="#ddd" stroke-width="1.5" fill="none"/></svg>
  <svg style="position:absolute;left:584px;top:1768px" width="12" height="24"><path d="m2 2 8 10-8 10" stroke="#ddd" stroke-width="1.5" fill="none"/></svg>
  <div class="avatar" role="img" aria-label="Portrait of a client hugging her husky"></div>
  <div class="author">- John Doe</div>

  <section class="info">
    <div class="badges"><div></div><div></div><div></div></div>
    <div class="member">CDTA PROFESSIONAL MEMBER #4821</div>
    <div class="info-icon" style="left:358px;top:44px"><svg width="20" height="20" viewBox="0 0 24 24"><path d="M6.6 10.8a15 15 0 0 0 6.6 6.6l2.2-2.2a1 1 0 0 1 1-.25 11 11 0 0 0 3.6.6 1 1 0 0 1 1 1V20a1 1 0 0 1-1 1A17 17 0 0 1 3 4a1 1 0 0 1 1-1h3.5a1 1 0 0 1 1 1 11 11 0 0 0 .6 3.6 1 1 0 0 1-.25 1z" fill="#555"/></svg></div>
    <div class="info-text" style="left:427px;top:45px">Phone No :  +702 - 555 - 0147<br>Email: hello@harlowk9.com</div>
    <div class="info-icon" style="left:655px;top:44px"><svg width="22" height="20" viewBox="0 0 22 20"><path d="M11 1 1 10h3v9h5v-6h4v6h5v-9h3z" fill="#555"/></svg></div>
    <div class="info-text" style="left:726px;top:45px">42 Harlow Ln Maplewood<br>Illinois 100482</div>
  </section>

  <footer class="footer">
    <nav>Home &nbsp;/&nbsp; About Us &nbsp;/&nbsp; Services &nbsp;/&nbsp; Photos / Videos &nbsp;/&nbsp; Get in Touch</nav>
    <p class="copy">Copyright © Harlow. All rights reserved.</p>
    <div class="social"><div></div><div></div><div></div><div></div><div></div></div>
  </footer>
</div>
</body>
</html>
```